Flyer-Design für Achtsamkeitscoaching
Zielgruppe
-Achtsamkeitscoaching - Stressbewältigung - Persönlichkeitsstärkung - Burnout Bewältigung
Aufgabenstellung
Faltflyer, 21 x 21cm, Titelseite: oberes Viertel soll 'härter' wirken - > anschließend in weichere Formen und Farbe übergehend, Grundfarbe = Pastell blaugrün, Logo + Akzente = Gold oder orange

```html
<!DOCTYPE html>
<html lang="de">
<head>
<meta charset="utf-8">
<title>Faltflyer Achtsamkeits-Coaching</title>
<link href="https://fonts.googleapis.com/css2?family=Roboto:wght@300;400;700&family=Kaushan+Script&family=Kalam:wght@700&display=swap" rel="stylesheet">
<style>
  :root{
    --stage:#9b9b9b;
    --green:#95c12b;
    --cream:#e7efc9;
    --gold:#d68d3c;
    --white:#ffffff;
    --text-dark:#ffffff;
    --photo-a:#3c6f8e;
    --photo-b:#1f3f5a;
    --skin-a:#8b5a3c;
    --skin-b:#6fc6d6;
  }
  *{box-sizing:border-box;margin:0;padding:0}
  html,body{width:1200px;height:600px;overflow:hidden}
  body{background:var(--stage);position:relative;font-family:"Roboto",Arial,sans-serif;color:var(--white)}
  .spread{position:absolute;top:10px;width:578px;height:578px;overflow:hidden}
  .spread--outside{left:15px;background:var(--green)}
  .spread--inside{left:607px;background:var(--cream)}
  .spread svg.shapes{position:absolute;inset:0}
  .abs{position:absolute}
  .copy{font-weight:300;font-size:9.2px;line-height:11.6px}
  .copy p+p{margin-top:8px}
  .justify{text-align:justify}
  .script{font-family:"Kaushan Script",cursive;color:var(--gold);line-height:1}
  .fold-line{position:absolute;left:289px;top:0;width:1px;height:578px;background:rgba(0,0,0,.06)}

  .intro{left:37px;top:26px;width:230px}
  .totem-title{left:160px;top:160px;font-size:37px;text-align:center;width:130px;transform:rotate(-6deg)}
  .dragonfly-photo{left:28px;top:200px;width:210px;height:155px}
  .permission{right:310px;top:360px;color:var(--gold);font-size:15.5px;text-align:right;line-height:19px}
  .walk-text{left:34px;top:433px;width:229px}
  .stress-questions{left:360px;top:28px;font-family:"Kalam",cursive;font-weight:700;font-size:28px;line-height:30px;letter-spacing:1.5px}
  .help-title{left:314px;top:172px;width:250px;font-size:44px;text-align:center}
  .brand-mark{left:330px;top:300px;width:210px;display:flex;align-items:center;justify-content:center;gap:10px;color:var(--gold);font-weight:700;font-size:20px}
  .brand-mark .dot{width:14px;height:14px;border-radius:50%;background:var(--gold)}
  .coach-block{left:300px;top:432px;width:270px;text-align:center}
  .coach-block h1{font-size:17.5px;font-weight:700;letter-spacing:.2px}
  .coach-block .coach-name{font-size:20px;font-weight:300;margin-top:4px}
  .coach-block .traits{font-weight:700;font-size:11.6px;line-height:14.6px;margin-top:9px;letter-spacing:.3px}
  .coach-block .credentials{font-weight:300;font-size:13px;line-height:16px;margin-top:8px}

  .fit-title{left:28px;top:10px;font-size:20px;line-height:22px;transform:rotate(-2deg)}
  .benefit-title{left:314px;top:10px;font-size:20px;line-height:22px;transform:rotate(-2deg)}
  .list-head{font-family:"Kaushan Script",cursive;color:var(--white);font-size:18px}
  .dash-list{list-style:none}
  .dash-list li{position:relative;padding-left:9px;font-weight:300;font-size:9.3px;line-height:11.6px;margin-bottom:9.4px}
  .dash-list li::before{content:"-";position:absolute;left:0}
  .yes-head{left:32px;top:92px}
  .yes-list{left:25px;top:115px;width:232px}
  .no-head{left:32px;top:318px}
  .no-list{left:25px;top:342px;width:130px}
  .coach-photo{left:104px;top:326px;width:266px;height:252px}
  .brand-mark--small{left:12px;top:462px;width:130px;display:flex;align-items:center;gap:7px;color:var(--white);font-weight:700;font-size:14px}
  .brand-mark--small .dot{width:10px;height:10px;border-radius:50%;background:var(--white)}
  .benefit-list{left:317px;top:100px;width:236px}
  .prejudice{left:317px;top:371px;width:232px}
  .prejudice h2{font-size:9.6px;font-weight:700;margin-bottom:8px}
  .contact{right:28px;top:470px;text-align:right}
  .contact .script{color:var(--white);font-size:21px}
  .contact .address{font-size:9.6px;font-weight:300;margin-top:8px}
</style>
</head>
<body>

<section class="spread spread--outside">
  <svg class="shapes" width="578" height="578" viewBox="0 0 578 578">
    <path d="M0,186 Q145,96 289,156 Q433,96 578,186 L578,360 Q433,440 289,400 Q145,440 0,360 Z" fill="var(--cream)" stroke="var(--white)" stroke-width="7"/>
    <path d="M0,186 Q145,96 289,156 Q433,96 578,186 L578,360 Q433,440 289,400 Q145,440 0,360 Z" fill="var(--cream)" stroke="var(--gold)" stroke-width="3.5"/>
  </svg>
  <div class="fold-line"></div>

  <div class="abs copy intro">
    <p>In einem kurzen Vorgespräch schauen wir in Deine Lebensbereiche, damit du einen IST - Stand für Dich erkennen kannst, an welchem du am Anfang Deiner Veränderung startest.</p>
    <p>Die Libelle fliegt in Dein Leben und bringt Dir Mut, Liebe und Zuversicht. Sie begleitet Dich.</p>
  </div>

  <svg class="abs dragonfly-photo" viewBox="0 0 210 155" role="img" aria-label="Foto einer blau schimmernden Libelle">
    <defs>
      <linearGradient id="dfly" x1="0" y1="0" x2="1" y2="1">
        <stop offset="0" stop-color="var(--photo-a)"/>
        <stop offset="1" stop-color="var(--photo-b)"/>
      </linearGradient>
    </defs>
    <ellipse cx="105" cy="78" rx="100" ry="70" fill="url(#dfly)" opacity=".55"/>
  </svg>

  <div class="abs script totem-title">Krafttier Libelle:</div>
  <div class="abs permission">ERLAUBNIS<br>zum Richtungswechsel</div>

  <div class="abs copy walk-text justify">
    <p>Gehe langsam, achtsam und bewusst Deine nächsten Schritte. Dein Leben richtet sich neu aus. Gehe mit, lasse das Alte los und erlaube Dir einen Richtungswechsel. Nimm Dein Leben in die Hand und schaffe Platz für Neues. Jetzt bist du bereit. Innerlich weißt du schon , in welchen Bereichen Du einen wirklichen Richtungswechsel brauchst.</p>
    <p>Höre Dir selbst zu, so bewältigst Du ganz leicht die Hürden, die auf Deinem Weg auf Dich warten.</p>
  </div>

  <div class="abs stress-questions">Gestresst?<br>Erschopft?<br>Genervt?</div>
  <div class="abs script help-title">Ich helfe Dir!</div>
  <div class="abs brand-mark"><span class="dot"></span>Lena Fardel</div>

  <div class="abs coach-block">
    <h1>ACHTSAMKEITS-COACHING</h1>
    <div class="coach-name">mit Lena Fardel</div>
    <div class="traits">kompetent und erfahren<br>ganzheitlich und flexibel<br>persönlich und vertraulich</div>
    <div class="credentials">Zertifizierte Achtsamkeitstrainerin und<br>KWB-geprüfte Stressmanagerin</div>
  </div>
</section>

<section class="spread spread--inside">
  <svg class="shapes" width="578" height="578" viewBox="0 0 578 578">
    <path d="M0,62 C80,72 200,82 300,74 C400,66 480,84 578,80 L578,528 C480,536 380,522 290,532 C200,540 90,520 0,520 Z" fill="var(--green)"/>
    <path d="M160,78 C220,75 280,72 330,76" stroke="var(--cream)" stroke-width="2" fill="none"/>
    <path d="M300,66 C380,60 470,70 560,78" stroke="var(--green)" stroke-width="4" fill="none"/>
    <path d="M380,532 C440,528 500,540 560,536" stroke="var(--cream)" stroke-width="2" fill="none"/>
  </svg>

  <div class="abs script fit-title">Ist mein Achtsamkeitscoaching<br>für dich geeignet ?</div>
  <div class="abs script benefit-title">Vorteile<br>Deines Coachings!</div>

  <div class="abs list-head yes-head">Yes! Wenn Du -</div>
  <ul class="abs dash-list yes-list">
    <li>raus willst, aus Deinem privaten und/ oder beruflichen Stress-Hamsterrad</li>
    <li>Dich müde, gereizt, verspannt, unruhig, wenig belastbar, unkonzentriert fühlst</li>
    <li>das Gefühl hast, in dieser schnelllebigen Zeit kurz zu kommen</li>
    <li>Dinge nicht nur verstehen, sondern auch Umsetzen willst</li>
    <li>nach Selbstvertrauen, Klarheit und innerer Ruhe strebst und bereit bist deine Komfortzone dafür zu verlassen</li>
    <li>wieder Du selbst werden möchtest und Dich wieder fühlen willst!</li>
  </ul>

  <div class="abs list-head no-head">No! Wenn Du -</div>
  <ul class="abs dash-list no-list">
    <li>nur einen kurzen Motivationskick suchst und nicht bereit bist Deine Verhaltensmuster zu hinterfragen</li>
    <li>keine Zeit und kein Geld in Dich investieren möchtest</li>
  </ul>

  <div class="abs brand-mark--small"><span class="dot"></span>Lena Fardel</div>

  <svg class="abs coach-photo" viewBox="0 0 266 252" role="img" aria-label="Porträtfoto der Coachin mit langen braunen Haaren und türkisem Oberteil">
    <defs>
      <linearGradient id="coachfill" x1="0" y1="0" x2="0" y2="1">
        <stop offset="0" stop-color="var(--skin-a)"/>
        <stop offset=".7" stop-color="var(--skin-a)"/>
        <stop offset="1" stop-color="var(--skin-b)"/>
      </linearGradient>
    </defs>
    <path d="M70,252 C70,200 60,120 80,60 C100,10 170,0 195,50 C215,100 205,190 266,252 Z" fill="url(#coachfill)" opacity=".75"/>
  </svg>

  <ul class="abs dash-list benefit-list">
    <li>Du wirst individuell und persönlich betreut.</li>
    <li>Herzlich und offen – ich begleite Dich, ohne Dich zu bewerten .</li>
    <li>Schneller Einstieg möglich. Keine Vorkenntnisse notwendig.</li>
    <li>Ganzheitlich – Ich bringe Dich nicht nur auf den Weg in die Achtsamkeit, sondern betrachte Deine Symptome auch in größeren Zusammenhängen</li>
    <li>Planbar – das Coaching findet einmal pro Woche im Zeitraum von acht Wochen statt –Nimm Dir die Zeit!</li>
    <li>Zielgruppe ALLE! – mein Coaching ist für dich geeignet, wenn Du dir sagst „Ich will es -- jetzt!“</li>
    <li>Das besondere Geschenk für Deine (n) Partnerin/ Partner, und die Krönung ist, wenn ihr es gemeinsam angeht. Liebe beruht auf Gegenseitigkeit.</li>
    <li>Ideal für Paare – es kann nur noch besser werden</li>
  </ul>

  <div class="abs prejudice">
    <h2>Ein Wort zu Vorurteilen:</h2>
    <p class="copy justify">Nein, es sind keine Hokuspokus-Stunden oder spirituelle Beweihräucherungen. Die Lehre der Achtsamkeit beruht auf langjährig erprobten und wissenschaftlich fundamentierten Erkenntnissen und ist längst in der modernen Arbeitswelt fest integriert .</p>
  </div>

  <div class="abs contact">
    <div class="script">Kontakt</div>
    <div class="address">Adresse</div>
  </div>
</section>

</body>
</html>
```